Golden Tempest graphic for firework company

I need a firework label. The title will be called GOLDEN TEMPEST. I will include some AI generated images. I like the image that has golden tempest written twice on the box. I like how it looks different. I like how stealthy the image looks. I have provided the template for the box as well.

Target Market(s)

teenagers, young adults, men

Industry/Entity Type

firework industry

Font styles to use
Other font styles liked:
• font used in graphic provided

Colors

Designer to choose colors to be used in the design.

Requirements
Must have
• I have include AI graphics. I would like the same feel, theme, color scheme. the illusion of the stealth bomber flying thru the clouds dropping the golden tempest and the fire and explosions coming off the golden tempest
Nice to have
• see uploaded design. I really like the way golden tempest is placed on the box top and bottom
Should not have
• can maybe use less wording. only use emerald whirl

```html
<!DOCTYPE html>
<html lang="en">
<head>
<meta charset="utf-8">
<title>Golden Tempest – Emerald Whirl Label</title>
<link rel="stylesheet" href="https://fonts.googleapis.com/css2?family=Saira+Condensed:wght@600;700;800&display=swap">
<style>
  :root {
    --page-bg: #ffffff;
    --sky-deep: #080a1e;
    --sky-mid: #1a1c46;
    --cloud-violet: #3b3366;
    --cloud-dusk: #5a4a78;
    --ember-orange: #e0782a;
    --ember-glow: #ffb45a;
    --burst-pink: #d0589e;
    --burst-violet: #8a6af0;
    --type-silver: #e6e6ee;
    --type-soft: #d4d4dc;
    --rule: #d0d0da;
  }
  * { margin: 0; padding: 0; box-sizing: border-box; }
  html, body {
    width: 1200px;
    height: 1001px;
    overflow: hidden;
    background: var(--page-bg);
  }
  .canvas {
    position: relative;
    width: 1200px;
    height: 1001px;
  }
  .label {
    position: absolute;
    left: 472px;
    top: 73px;
    width: 256px;
    height: 860px;
    overflow: hidden;
    font-family: "Saira Condensed", "Arial Narrow", sans-serif;
    text-align: center;
  }
  .label__artwork {
    position: absolute;
    inset: 0;
    background:
      radial-gradient(ellipse 60% 10% at 40% 66%, rgba(90,74,120,0.55), transparent 80%),
      radial-gradient(ellipse 70% 9% at 70% 74%, rgba(59,51,102,0.7), transparent 80%),
      radial-gradient(ellipse 55% 8% at 25% 80%, rgba(90,74,120,0.5), transparent 80%),
      radial-gradient(ellipse 50% 12% at 75% 20%, rgba(90,74,120,0.45), transparent 80%),
      linear-gradient(180deg, var(--sky-deep) 0%, var(--sky-mid) 35%, #14153a 60%, #1c1a44 78%, var(--sky-deep) 100%);
  }
  .glow {
    position: absolute;
    border-radius: 50%;
  }
  .glow--ember-main {
    left: -60px; top: 120px; width: 220px; height: 120px;
    background: radial-gradient(ellipse at center, rgba(255,180,90,0.9), rgba(224,120,42,0.45) 40%, transparent 72%);
    transform: rotate(-18deg);
  }
  .glow--ember-streak-a {
    left: 10px; top: 30px; width: 240px; height: 26px;
    background: radial-gradient(ellipse at center, rgba(255,160,70,0.7), transparent 70%);
    transform: rotate(-12deg);
  }
  .glow--ember-streak-b {
    left: -30px; top: 220px; width: 260px; height: 22px;
    background: radial-gradient(ellipse at center, rgba(255,150,60,0.65), transparent 70%);
    transform: rotate(-16deg);
  }
  .glow--ember-streak-c {
    left: 40px; top: 80px; width: 200px; height: 18px;
    background: radial-gradient(ellipse at center, rgba(240,130,50,0.55), transparent 70%);
    transform: rotate(-20deg);
  }
  .glow--title-burst {
    left: 0; top: 270px; width: 256px; height: 190px;
    background: radial-gradient(ellipse at center, rgba(138,106,240,0.7), rgba(208,88,158,0.35) 40%, transparent 70%);
  }
  .glow--base-burst {
    left: -30px; top: 700px; width: 316px; height: 200px;
    background: radial-gradient(ellipse at 50% 75%, rgba(208,88,158,0.75), rgba(138,106,240,0.3) 45%, transparent 72%);
  }
  .brand {
    position: absolute;
    left: 0;
    right: 0;
    top: 300px;
    color: var(--type-silver);
    font-weight: 800;
    font-size: 60px;
    line-height: 0.86;
    letter-spacing: 0;
  }
  .product-name {
    position: absolute;
    left: 22px;
    right: 22px;
    top: 496px;
    padding: 2px 0 1px;
    border-top: 1px solid var(--rule);
    border-bottom: 1px solid var(--rule);
    color: var(--type-silver);
    font-weight: 700;
    font-size: 31px;
    line-height: 1.02;
    letter-spacing: 0.4px;
  }
  .tagline {
    position: absolute;
    left: 0;
    right: 0;
    top: 544px;
    color: var(--type-soft);
    font-weight: 600;
    font-size: 16px;
    line-height: 21px;
    letter-spacing: 1.3px;
  }
  .tagline strong {
    display: block;
    font-weight: 700;
    font-size: 18px;
    color: var(--type-silver);
  }
</style>
</head>
<body>
  <main class="canvas">
    <section class="label">
      <div class="label__artwork" role="img" aria-label="Night sky with drifting clouds, golden sparks streaking across the top and violet firework bursts behind the title and along the bottom edge">
        <div class="glow glow--ember-streak-a"></div>
        <div class="glow glow--ember-streak-c"></div>
        <div class="glow glow--ember-main"></div>
        <div class="glow glow--ember-streak-b"></div>
        <div class="glow glow--title-burst"></div>
        <div class="glow glow--base-burst"></div>
      </div>
      <h1 class="brand">GOLDEN<br>TEMPEST</h1>
      <h2 class="product-name">EMERALD WHIRL</h2>
      <p class="tagline">WHEN THE SKY GOES DARK,<strong>THE TEMPEST FALLS</strong></p>
    </section>
  </main>
</body>
</html>
```